Wellness Thai Massage Geschäft benötigt eine Preis/Info Broschüre

Ein kleines Thai Massage Geschäft in Bayern: Sukonta Thaimassage
Benötigt eine kleine Preisliste, sowie eine kurze Beschreibung vom Unternehmen. Angeboten werden traditionelle Thaimassagen. Der Farbstil soll dem Logo (Anhang) angepasst sein. Alle Bilder außer die Bilder von der Geschäftsführerin sind optional zur Verwendung verfügbar. Mehr Info wie Preise, etc. sind verfügbar auf der Website https://www.sukontathaimassage-beispiel.de/

```html
<!DOCTYPE html>
<html lang="en">
<head>
<meta charset="utf-8">
<title>Sukonta Thaimassage – Trifold Brochure</title>
<link rel="stylesheet" href="https://fonts.googleapis.com/css2?family=Montserrat:wght@400;500;600;700&family=Oswald:wght@500&family=Playfair+Display:wght@900&display=swap">
<style>
  :root{
    --maroon:#8b1c22;
    --maroon-dark:#6a1217;
    --cream:#eee5b8;
    --cream-light:#f6efcf;
    --peach:#e6a284;
    --pill:#f6e6a6;
    --paper:#ececec;
    --ink:#2a2220;
    --white:#ffffff;
    --stage:#e9e9e9;
  }
  *{box-sizing:border-box;margin:0;padding:0}
  html,body{width:834px;height:1200px;overflow:hidden;background:var(--stage)}
  body{position:relative;font-family:"Montserrat",sans-serif;color:var(--ink)}
  .sheet{position:absolute;left:27px;width:780px;height:552px;overflow:hidden;box-shadow:0 4px 14px rgba(0,0,0,.18)}
  .sheet--outside{top:32px;background:var(--cream)}
  .sheet--inside{top:616px;background:var(--paper)}
  .sheet__bg{position:absolute;inset:0;width:100%;height:100%}
  .abs{position:absolute}
  .photo{position:absolute;border-radius:50%;border:2px solid var(--ink)}
  .label{position:absolute;font-family:"Oswald",sans-serif;font-size:15px;color:var(--ink);border:1.5px solid var(--maroon);padding:1px 8px;letter-spacing:.3px;background:var(--white)}
  .body-copy{font-size:8.6px;line-height:1.5;font-weight:500}
  .hours p{font-size:9px;font-weight:600;line-height:1.35;border-left:2px solid var(--maroon);padding-left:6px;margin-bottom:4px}
  .contact li{list-style:none;font-size:9px;font-weight:600;display:flex;align-items:center;gap:7px;margin-bottom:7px}
  .contact svg{width:11px;height:11px;flex:none}
  .brand{position:absolute;left:560px;top:26px;display:flex;align-items:center;gap:10px}
  .brand__dot{width:26px;height:26px;border-radius:50%;background:#e7a9c6}
  .brand__name{font-size:13px;font-weight:600;color:var(--cream);line-height:1.2;letter-spacing:1px;text-transform:uppercase}
  .welcome{position:absolute;left:540px;top:330px;width:230px;text-align:center;color:var(--maroon)}
  .welcome h1{font-family:"Playfair Display",serif;font-size:30px;line-height:1}
  .welcome h2{font-family:"Playfair Display",serif;font-size:14px;margin-top:3px}
  .welcome .tagline{display:inline-block;margin-top:8px;font-family:"Oswald",sans-serif;font-size:11px;color:var(--ink);border:1px solid var(--maroon);padding:2px 10px}
  .service{position:absolute;width:235px}
  .service h3{font-size:16px;font-weight:700;color:var(--maroon);line-height:1.15;border-left:2px solid var(--maroon);padding-left:8px;margin-bottom:5px}
  .service p{font-size:7.6px;line-height:1.45;font-weight:500;margin-bottom:8px}
  .price{display:flex;align-items:center;margin-bottom:5px}
  .price__time{background:var(--pill);color:var(--maroon);font-weight:700;font-size:11px;padding:3px 14px;border-radius:12px;width:110px}
  .price__amount{background:var(--maroon);color:var(--white);font-weight:700;font-size:11px;padding:3px 12px;border-radius:12px;margin-left:-8px}
  .intro{position:absolute;left:32px;top:338px;width:220px}
  .intro h2{font-size:17px;font-weight:500;line-height:1.15;border-left:2px solid var(--maroon);padding-left:8px}
  .intro h2 strong{color:var(--maroon);font-weight:700;font-size:19px}
  .intro p{margin-top:10px}
</style>
</head>
<body>

<section class="sheet sheet--outside">
  <svg class="sheet__bg" viewBox="0 0 780 552" preserveAspectRatio="none" aria-hidden="true">
    <defs>
      <linearGradient id="wave" x1="0" x2="1"><stop offset="0" stop-color="#e59a80"/><stop offset=".45" stop-color="#a2403e"/><stop offset="1" stop-color="#8b1c22"/></linearGradient>
    </defs>
    <path d="M0 0H780V150C700 250 620 170 540 200C440 240 380 80 300 150C200 70 80 140 0 90Z" fill="url(#wave)"/>
    <rect x="520" y="0" width="260" height="90" fill="var(--maroon)"/>
    <path d="M0 120C40 90 170 60 265 150V552H40C10 500 0 420 0 380Z" fill="var(--white)"/>
    <path d="M520 470C600 420 700 440 780 420V552H520Z" fill="var(--maroon)"/>
    <path d="M0 510C60 552 260 560 340 500C420 460 460 490 520 490V552H0Z" fill="var(--peach)" opacity=".45"/>
    <path d="M20 505C60 545 230 560 330 500" fill="none" stroke="var(--ink)" stroke-width="1.5"/>
    <line x1="260" y1="0" x2="260" y2="552" stroke="#000" stroke-opacity=".06"/>
    <line x1="520" y1="0" x2="520" y2="552" stroke="#000" stroke-opacity=".06"/>
  </svg>

  <div class="photo" style="left:45px;top:60px;width:210px;height:210px;background:radial-gradient(circle at 45% 45%,#b8a79a,#4a4440 70%)" role="img" aria-label="Photo of herbal compress, oils and rolled towel"></div>
  <div class="abs" style="left:40px;top:230px;width:70px;height:50px;border-radius:50%;background:#f4f0e0" role="img" aria-label="Frangipani flowers"></div>

  <div class="label" style="left:30px;top:300px">ABOUT US</div>
  <p class="body-copy abs" style="left:30px;top:332px;width:225px">Sukonta Thaimassage attaches great importance to the satisfaction and well-being of each customer. If, for example, you are stressed after a lot of work and pain has built up in a certain region, then you have come to the right place. The massage studio is run by Malee Beispiel, who was professionally trained and has also gained a lot of professional experience in Germany and Thailand. We look forward to your visit at Sukonta Thaimassage!</p>
  <div class="abs" style="left:140px;top:496px;width:110px;height:44px;border-radius:40%;background:linear-gradient(135deg,#c9b07a,#3a3a3a)" role="img" aria-label="Hot stones with oil bottle and orchid"></div>

  <div class="label" style="left:290px;top:225px">OPENING HOURS:</div>
  <div class="hours abs" style="left:292px;top:262px">
    <p>Monday:<br>9.00 a.m. - 8.00 p.m</p>
    <p>Tuesday - Friday:<br>10.00 a.m. - 8.00 p.m</p>
    <p>Saturday:<br>10.00 a.m. - 6.00 p.m</p>
    <p>Closed Sundays</p>
  </div>
  <div class="abs" style="left:415px;top:280px;width:95px;height:65px;border-radius:45%;background:linear-gradient(160deg,#6b8f4a,#222)" role="img" aria-label="Stacked black stones with bamboo leaves"></div>

  <div class="label" style="left:290px;top:368px">CONTACT INFO</div>
  <ul class="contact abs" style="left:292px;top:404px">
    <li><svg viewBox="0 0 12 12"><path d="M6 1a3.5 3.5 0 0 0-3.5 3.5C2.5 7 6 11 6 11s3.5-4 3.5-6.5A3.5 3.5 0 0 0 6 1z" fill="var(--maroon)"/></svg>Beispielweg 12<br>Musterstadt 83600</li>
    <li><svg viewBox="0 0 12 12"><rect x="1" y="2.5" width="10" height="7" fill="none" stroke="var(--maroon)"/><path d="M1 2.5l5 4 5-4" fill="none" stroke="var(--maroon)"/></svg>sukonta.thaimassage@beispiel.de</li>
    <li><svg viewBox="0 0 12 12"><circle cx="6" cy="6" r="5" fill="none" stroke="var(--maroon)"/><path d="M4 3.5l1 1-.5 1 1.5 1.5 1-.5 1 1-1 1C5 8 4 7 3.5 4.5z" fill="var(--maroon)"/></svg>+49 170 0000000</li>
    <li><svg viewBox="0 0 12 12"><circle cx="6" cy="6" r="5" fill="none" stroke="var(--maroon)"/><path d="M1 6h10M6 1c-2 3-2 7 0 10M6 1c2 3 2 7 0 10" fill="none" stroke="var(--maroon)"/></svg>www.sukontathaimassage-beispiel.de</li>
  </ul>

  <div class="brand"><span class="brand__dot"></span><span class="brand__name">Sukonta<br>Thaimassage</span></div>
  <div class="photo" style="left:560px;top:110px;width:190px;height:190px;background:radial-gradient(circle at 50% 40%,#5a4a40,#c0504a 70%)" role="img" aria-label="Buddha statue with red flower petals"></div>
  <div class="welcome">
    <h1>Welcome to</h1>
    <h2>Sukonta's Thai massage</h2>
    <span class="tagline">TRADITIONAL THAI MASSAGES SPECIALIST</span>
  </div>
</section>

<section class="sheet sheet--inside">
  <svg class="sheet__bg" viewBox="0 0 780 552" preserveAspectRatio="none" aria-hidden="true">
    <path d="M520 0H780V552H560C640 460 600 300 680 200C720 130 640 60 520 60Z" fill="var(--cream)" opacity=".8"/>
    <circle cx="410" cy="120" r="70" fill="var(--pill)"/>
    <path d="M40 60C60 0 230 0 360 30C380 120 340 190 280 200C200 220 60 170 40 60Z" fill="var(--maroon)"/>
    <path d="M0 528C120 552 300 548 360 522C420 500 470 512 520 505V552H0Z" fill="var(--maroon)"/>
    <path d="M520 505C620 490 700 505 780 490V552H520Z" fill="var(--maroon-dark)" opacity=".9"/>
    <path d="M20 200C30 130 80 90 130 90" fill="none" stroke="var(--ink)" stroke-width="1.3"/>
    <path d="M520 500C600 500 700 498 760 470" fill="none" stroke="var(--ink)" stroke-width="1.3"/>
    <line x1="260" y1="0" x2="260" y2="552" stroke="#000" stroke-opacity=".06"/>
    <line x1="520" y1="0" x2="520" y2="552" stroke="#000" stroke-opacity=".06"/>
  </svg>

  <div class="photo" style="left:20px;top:60px;width:250px;height:250px;background:radial-gradient(circle at 45% 50%,#c6a070,#7a3a2a 75%)" role="img" aria-label="Photo of a therapist giving a Thai stretching massage"></div>
  <div class="abs" style="left:190px;top:282px;width:90px;height:48px;border-radius:40%;background:linear-gradient(135deg,#d8c49a,#888)" role="img" aria-label="Rolled towel with stacked stones"></div>
  <div class="intro">
    <h2>what is<br><strong>Thai Massage</strong><br>actually?</h2>
    <p class="body-copy">Thai massage has existed for more than 2500 years, which over time has developed into an effective method against pain and diseases, which has even achieved cult status today. This Thai healing method requires professional training that involves background knowledge and long training.</p>
  </div>

  <div class="photo" style="left:245px;top:-10px;width:190px;height:190px;background:radial-gradient(circle at 50% 50%,#333,#d8c8a8 75%)" role="img" aria-label="Massage cream jars and stacked hot stones"></div>

  <div class="service" style="left:282px;top:190px">
    <h3>Traditional<br>Thai sports massage</h3>
    <p>With the traditional Thai massage, energy blockages are released through acupressure, stretching and energy line massage. 10 energy points and lines that are important for the harmony of body and mind are massaged. Thus an inner balance and the flow of life energy is achieved.</p>
    <div class="price"><span class="price__time">60 minutes</span><span class="price__amount">€54</span></div>
    <div class="price"><span class="price__time">90 minutes</span><span class="price__amount">€76</span></div>
  </div>
  <div class="service" style="left:282px;top:362px">
    <h3>Aroma oil massage</h3>
    <p>The aroma oil massage is a form of treatment to regenerate and harmonize the entire body. The base oil is enriched with essential oils. Aromatherapy can be adjusted to be stimulating or relaxing.</p>
    <div class="price"><span class="price__time">60 minutes</span><span class="price__amount">€51</span></div>
    <div class="price"><span class="price__time">90 minutes</span><span class="price__amount">€72</span></div>
  </div>
  <div class="abs" style="left:440px;top:488px;width:80px;height:40px;border-radius:40%;background:linear-gradient(135deg,#a05a2a,#9a7ac0)" role="img" aria-label="Essential oil bottle with lavender"></div>

  <div class="service" style="left:535px;top:22px">
    <h3>Hot stone massage</h3>
    <p>During the hot stone massage, warmed volcanic stones are placed along the energy lines. The energy flow and blood circulation are increased by the released stored heat. Deep relaxation occurs throughout the body.</p>
    <div class="price"><span class="price__time">90 minutes</span><span class="price__amount">€83</span></div>
  </div>
  <div class="service" style="left:535px;top:160px">
    <h3>Foot<br>reflexology massage</h3>
    <p>A massage for what is probably the most stressed part of the body, the feet, releases new strength and gives vitality.</p>
    <div class="price"><span class="price__time">30 minutes</span><span class="price__amount">€35</span></div>
    <div class="price"><span class="price__time">60 minutes</span><span class="price__amount">€62</span></div>
  </div>
  <div class="service" style="left:535px;top:300px">
    <h3>Back Thai massage</h3>
    <p>This massage technique mostly involves the back, as well as the neck, back of the head, shoulders and fingers. This massage is particularly suitable if one of these areas is tense or causing pain.</p>
    <div class="price"><span class="price__time">30 minutes</span><span class="price__amount">€35</span></div>
    <div class="price"><span class="price__time">60 minutes</span><span class="price__amount">€72</span></div>
  </div>
  <div class="abs" style="left:695px;top:448px;width:75px;height:44px;border-radius:40%;background:linear-gradient(135deg,#f4f4f4,#6a9a4a)" role="img" aria-label="Towel, herbs and stones"></div>
</section>

</body>
</html>
```